Occupational Medical Billing and Coding Business needs Postcard

Medical billing and coding business needs marketing postcard to send to target audience of orthopaedic surgeons who practice medicine in California Workers' Compensation industry. These doctors treat injured workers and/or provide medical-legal evaluations and reports for the courts to settle the injured worker's claim. This is a highly specialized area of medical billing and coding. It is extremely complicated and can be very frustrating for doctors and their staff who do not understand the system. I would encourage the designers to check out my website: www.CorvaleHealthClaims.com
I want something bright and colorful that makes bold statements. It has to get their attention. My suggestions for bold statements include:
1) QMEs! Are your bills compliant with DWC's view? We make sure your complexity factors are maximized as well as compliant.
2) We collected over $ 462,000 just in second bill review (SBR) appeals alone and that's just one orthopaedic surgeon! Imagine what we can do for you!

I uploaded a word document with some information about the services I offer. The company logo is also there. Let me know if you need it in another format. The items with the asterisk (**) must be in the postcard.

Thank you so much!

Corvale Health Claims

Target Market(s)

Orthopaedic Surgeons who treat injured workers in California

Font styles to use
Sans Serif

Colors

Designer to choose colors to be used in the design.

Requirements
Must have
• Expert Billing and Coding Services for:
• QME - AME - IME Evaluations
• Radiology - MRI/CT Scans
• Orthopaedic Surgery
• Certified Coders on Staff
• Electronic Claim Submission
• Payment within 15 days
• It's important to spell orthopaedic with the "A" after the "P" as it is an acknowledgment of the origins of the practice and will attract a doctor with higher education.

```html
<!DOCTYPE html>
<html lang="en">
<head>
<meta charset="utf-8">
<title>Corvale Health Claims Postcard</title>
<link href="https://fonts.googleapis.com/css2?family=Open+Sans:wght@400;600;700;800&display=swap" rel="stylesheet">
<style>
  :root{
    --blue:#1f78c8;
    --blue-dark:#125fa6;
    --peach:#f7d1b0;
    --peach-soft:#fbe6d4;
    --ink:#1c2b3a;
    --white:#ffffff;
    --page:#ffffff;
  }
  *{box-sizing:border-box;margin:0;padding:0}
  html,body{width:880px;height:1200px;overflow:hidden;background:var(--page);font-family:"Open Sans",Arial,sans-serif;color:var(--ink)}
  .card{position:absolute;left:15px;width:850px;height:507px;background:var(--white);overflow:hidden;box-shadow:0 2px 8px rgba(0,0,0,.25)}
  .card--front{top:35px}
  .card--back{top:620px}
  .stripes{position:absolute;inset:0}
  .abs{position:absolute}
  .headline{left:24px;top:16px;width:420px;font-size:23px;line-height:1.22;font-weight:800;color:var(--blue)}
  .brand{right:24px;top:52px;display:flex;align-items:center;gap:8px;font-size:14px;font-weight:700;color:var(--blue-dark);white-space:nowrap}
  .brand-dot{width:13px;height:13px;border-radius:50%;background:var(--blue-dark)}
  .office-photo{left:340px;top:108px;width:510px;height:287px;background:linear-gradient(135deg,#eef1f4 0%,#dde3ea 55%,#f5f6f8 100%)}
  .panel{background:var(--blue);color:var(--white)}
  .panel-head{background:var(--peach);color:var(--blue-dark);font-weight:700;padding:6px 14px}
  .services{left:30px;top:138px;width:310px;height:262px}
  .services .panel-head{font-size:14.5px}
  .list{list-style:none;padding:10px 16px 0 18px}
  .list li{position:relative;padding-left:14px;font-size:12.5px;line-height:1.3;margin-bottom:2px}
  .list li::before{content:"";position:absolute;left:0;top:6px;width:6px;height:6px;background:var(--white)}
  .call{left:340px;top:402px;font-size:36px;font-weight:600;color:var(--blue);white-space:nowrap}
  .footer-bar{left:0;bottom:0;width:850px;height:44px;background:var(--blue);display:flex;align-items:center;gap:120px;padding-left:44px;color:var(--white);font-size:13px}
  .contact-item{display:flex;align-items:center;gap:8px}
  .contact-item svg{width:14px;height:14px;flex:none}
  .collections{left:20px;top:60px;width:440px;height:410px}
  .collections .panel-head{font-size:15px}
  .collections .list li{font-size:12.5px;margin-bottom:14px}
  .contact-head{margin-top:8px}
  .contact-list{padding:10px 18px;font-size:12.5px;line-height:1.6}
  .stamp{right:40px;top:36px;width:82px;height:96px;border:2px dashed #9aa6b2}
  .address-line{left:560px;width:250px;height:2px;background:#9aa6b2}
</style>
</head>
<body>

<section class="card card--front">
  <svg class="stripes" viewBox="0 0 850 507" aria-hidden="true">
    <polygon points="470,0 530,0 430,395 370,395" fill="var(--peach-soft)"/>
    <polygon points="540,0 590,0 490,395 440,395" fill="var(--blue)"/>
    <polygon points="605,0 625,0 525,395 505,395" fill="var(--blue-dark)"/>
    <rect x="0" y="395" width="850" height="70" fill="var(--peach-soft)"/>
  </svg>
  <div class="abs office-photo" role="img" aria-label="Bright modern medical office interior"></div>
  <h1 class="abs headline">Medical Billing &amp; Collections for California Workers' Compensation Providers</h1>
  <div class="abs brand"><span class="brand-dot"></span>Corvale Health Claims</div>
  <div class="abs panel services">
    <div class="panel-head">Expert Billing and Coding Services for:</div>
    <ul class="list">
      <li>QME - AME - IME Evaluations<br>Treatment - Primary/Secondary Physician</li>
      <li>Radiology - MRI/CT Scans<br>Electrodiagnostic Studies</li>
      <li>Orthopaedic Surgery<br>Ambulatory Surgery Centers</li>
      <li>Certified Coders on Staff</li>
      <li>Electronic Claim Submission</li>
      <li>Payment within 15 days</li>
      <li>Over 25 Years Experience in Workers' Comp</li>
    </ul>
  </div>
  <div class="abs call">Call Today: 714.555.0182</div>
  <div class="abs footer-bar">
    <span class="contact-item"><svg viewBox="0 0 16 16"><rect x="1" y="3" width="14" height="10" fill="none" stroke="#fff" stroke-width="1.5"/><polyline points="1,3 8,9 15,3" fill="none" stroke="#fff" stroke-width="1.5"/></svg>info@CorvaleHealthClaims.com</span>
    <span class="contact-item"><svg viewBox="0 0 16 16"><circle cx="8" cy="8" r="6.5" fill="none" stroke="#fff" stroke-width="1.5"/><line x1="1.5" y1="8" x2="14.5" y2="8" stroke="#fff" stroke-width="1.2"/><ellipse cx="8" cy="8" rx="3" ry="6.5" fill="none" stroke="#fff" stroke-width="1.2"/></svg>www.CorvaleHealthClaims.com</span>
  </div>
</section>

<section class="card card--back">
  <svg class="stripes" viewBox="0 0 850 507" aria-hidden="true">
    <polygon points="0,0 180,0 60,507 0,507" fill="var(--peach-soft)"/>
    <polygon points="440,0 500,0 400,507 340,507" fill="var(--blue-dark)"/>
  </svg>
  <div class="abs panel collections">
    <div class="panel-head">We also provide Collection Services:</div>
    <ul class="list">
      <li>Expert Denial Management: Timely filing of SBR and IBR Appeals - Collected over $462,000 just in second bill review appeals. This is an example of ONE orthopaedic surgeon to date. Imagine what we can do for you!</li>
      <li>Don't let insurance companies "zero-out" your QME and AME bills. We get your medical-legal bills paid including penalty, interest and costs associated with the effort to collect.</li>
    </ul>
    <div class="panel-head contact-head">Contact Us</div>
    <div class="contact-list">
      <div class="contact-item"><svg viewBox="0 0 16 16"><path d="M4 1l3 3-2 2c1 2 3 4 5 5l2-2 3 3-2 3C7 15 1 9 1 3z" fill="#fff"/></svg>714.555.0182</div>
      <div class="contact-item"><svg viewBox="0 0 16 16"><rect x="1" y="3" width="14" height="10" fill="none" stroke="#fff" stroke-width="1.5"/><polyline points="1,3 8,9 15,3" fill="none" stroke="#fff" stroke-width="1.5"/></svg>info@CorvaleHealthClaims.com</div>
      <div class="contact-item"><svg viewBox="0 0 16 16"><circle cx="8" cy="8" r="6.5" fill="none" stroke="#fff" stroke-width="1.5"/><line x1="1.5" y1="8" x2="14.5" y2="8" stroke="#fff" stroke-width="1.2"/><ellipse cx="8" cy="8" rx="3" ry="6.5" fill="none" stroke="#fff" stroke-width="1.2"/></svg>www.CorvaleHealthClaims.com</div>
    </div>
  </div>
  <div class="abs stamp"></div>
  <div class="abs address-line" style="top:270px"></div>
  <div class="abs address-line" style="top:305px"></div>
  <div class="abs address-line" style="top:340px"></div>
  <div class="abs address-line" style="top:375px"></div>
</section>

</body>
</html>
```